Brightwell Dwellings

Design a stylish Business card- we would like a businness card design that suits plastic business cards. Our card needs to show that we are tech savy and technology based so the design is crucial.

Target Market(s)

22-40

Industry/Entity Type

Plastic

Requirements
Must have
• attached is our logo. also double sided card would be nice.
my details

Callum Fenwright
Director
0461927345
www.brightwelldwellings.com.au
17 Marlow Crest Avenue, West Perth

```html
<!DOCTYPE html>
<html lang="en">
<head>
<meta charset="utf-8">
<title>Brightwell Dwellings – Business Card</title>
<link rel="stylesheet" href="https://fonts.googleapis.com/css2?family=Orbitron:wght@500;700;900&family=Cormorant+Garamond:wght@500&display=swap">
<style>
  :root {
    --page-bg: #d6d6d6;
    --card-black: #050505;
    --card-grey: #3a3a3a;
    --panel-black: #020202;
    --brand-blue: #2aa7d8;
    --text-white: #f2f2f2;
    --text-grey: #b5b5b5;
    --label-ink: #2b2b2b;
  }
  html, body {
    margin: 0;
    padding: 0;
    width: 1200px;
    height: 765px;
    overflow: hidden;
    background: var(--page-bg);
  }
  .canvas {
    position: relative;
    width: 1200px;
    height: 765px;
  }
  .card {
    position: absolute;
    top: 302px;
    width: 574px;
    height: 343px;
    border-radius: 32px;
    overflow: hidden;
    background: var(--card-black);
    box-shadow: 0 10px 24px rgba(0,0,0,0.35);
  }
  .card--front { left: 16px; }
  .card--back { left: 604px; }
  .card__texture {
    position: absolute;
    inset: 0;
    background: radial-gradient(ellipse at 70% 40%, #6a6a6a 0%, var(--card-grey) 35%, var(--card-black) 80%);
  }
  .card--back .card__texture {
    background: linear-gradient(180deg, #2e2e2e 0%, #4a4a4a 40%, #111 75%, var(--card-black) 100%);
  }
  .logo-panel {
    position: absolute;
    left: 0;
    top: 90px;
    width: 389px;
    height: 164px;
    background: var(--panel-black);
    border-radius: 0 22px 22px 0;
    box-shadow: 0 4px 12px rgba(0,0,0,0.6);
    display: flex;
    align-items: center;
    gap: 16px;
    padding-left: 40px;
    box-sizing: border-box;
  }
  .logo-panel__mark {
    width: 22px;
    height: 22px;
    background: var(--brand-blue);
    flex: none;
  }
  .logo-panel__name {
    font-family: "Orbitron", sans-serif;
    font-weight: 900;
    font-size: 30px;
    line-height: 1.15;
    color: var(--brand-blue);
    margin: 0;
    letter-spacing: 0.5px;
  }
  .contact {
    position: absolute;
    left: 38px;
    top: 164px;
    right: 20px;
    font-family: "Orbitron", sans-serif;
    color: var(--text-white);
  }
  .contact__mark {
    position: absolute;
    left: 0;
    top: 8px;
    width: 36px;
    height: 36px;
    border: 2px solid var(--text-white);
    box-sizing: border-box;
  }
  .contact__name {
    margin: 0 0 0 50px;
    font-weight: 900;
    font-size: 28px;
    letter-spacing: 1px;
    line-height: 1;
    text-transform: uppercase;
  }
  .contact__role {
    margin: 2px 0 0 50px;
    font-weight: 500;
    font-size: 17px;
    letter-spacing: 3px;
    color: var(--text-grey);
    text-transform: uppercase;
  }
  .contact__line {
    margin: 0 0 0 50px;
    font-weight: 500;
    font-size: 10.5px;
    letter-spacing: 1px;
    text-transform: uppercase;
    white-space: nowrap;
  }
  .contact__line--email { margin-top: 10px; }
  .contact__line--phone { margin-top: 24px; }
  .contact__line--address { margin-top: 10px; }
  .contact__sep { margin: 0 16px; }
  .side-label {
    position: absolute;
    top: 684px;
    font-family: "Cormorant Garamond", serif;
    font-weight: 500;
    font-size: 15px;
    letter-spacing: 3px;
    color: var(--label-ink);
  }
  .side-label--front { left: 66px; }
  .side-label--back { left: 660px; }
</style>
</head>
<body>
<div class="canvas">
  <section class="card card--front">
    <div class="card__texture" role="img" aria-label="Dark grid of glowing window panes as card background texture"></div>
    <div class="logo-panel">
      <span class="logo-panel__mark"></span>
      <h1 class="logo-panel__name">BRIGHTWELL<br>DWELLINGS</h1>
    </div>
  </section>

  <section class="card card--back">
    <div class="card__texture" role="img" aria-label="Dark grid of glowing window panes as card background texture"></div>
    <div class="contact">
      <span class="contact__mark"></span>
      <h2 class="contact__name">Callum Fenwright</h2>
      <p class="contact__role">Director</p>
      <p class="contact__line contact__line--email">callum@brightwelldwellings.com.au<span class="contact__sep">|</span>94183062</p>
      <p class="contact__line contact__line--phone">0461927345<span class="contact__sep">|</span>www.brightwelldwellings.com.au</p>
      <p class="contact__line contact__line--address">17 Marlow Crest Avenue, West Perth</p>
    </div>
  </section>

  <span class="side-label side-label--front">FRONT</span>
  <span class="side-label side-label--back">BACK</span>
</div>
</body>
</html>
```